VELQUARTH - A modern gin bottle label

Design of a bottle label in a modern fresh design. The name of the gin is "VELQUARTH Hollow Batch K7". Please take a look at the velquarth.de website. on the main page of velquarth.de you can breathe the design direction here: 1) the taste of the gin should be composed of 10 botanicals ... an important scent note. ) a distinctive flavor is spicy and fresh 3.) The filling volume is 0.5 liters 4.) the alcohol content is 43% vol. 5.) the variety is called "dry gin" 6.) velquarth stands for "energy" and "love"

Target Market(s)

Alcohol consumer

Colors

Designer to choose colors to be used in the design.

Requirements
Must have
• the velquarth corporate logo must be included, the name of the gin is "VELQUARTH Hollow Batch K7"
Nice to have
• Please use the bottles template in the appendix. (The Black Bottles) they can use the saying "DESTILLED & BOTTLED BY OLD MARROW" in small letters

```html
<!DOCTYPE html>
<html lang="en">
<head>
<meta charset="utf-8">
<title>VELQUARTH Hollow Batch K7 – Label</title>
<link rel="stylesheet" href="https://fonts.googleapis.com/css2?family=Michroma&family=Marcellus&display=swap">
<style>
  :root {
    --label-black: #0c0912;
    --label-ink: #15101d;
    --logo-white: #e9e9ee;
    --orange-deep: #c4431b;
    --orange-mid: #d8691f;
    --amber: #e9a12b;
    --muted-grey: #9c98a4;
  }
  * { box-sizing: border-box; margin: 0; padding: 0; }
  html, body {
    width: 900px;
    height: 1200px;
    overflow: hidden;
    background: var(--label-black);
  }
  .label {
    position: relative;
    width: 900px;
    height: 1200px;
    background: radial-gradient(ellipse at 50% 35%, var(--label-ink) 0%, var(--label-black) 70%);
    display: flex;
    flex-direction: column;
    align-items: center;
    font-family: "Marcellus", serif;
    text-align: center;
  }
  .brand {
    margin-top: 300px;
    display: flex;
    flex-direction: column;
    align-items: center;
    gap: 34px;
  }
  .brand-dot {
    width: 70px;
    height: 70px;
    border-radius: 50%;
    background: var(--orange-mid);
  }
  .brand-name {
    font-family: "Michroma", sans-serif;
    font-size: 64px;
    letter-spacing: 10px;
    color: var(--logo-white);
  }
  .variety {
    margin-top: 70px;
  }
  .variety-flavour {
    font-size: 46px;
    color: var(--orange-mid);
    letter-spacing: 1px;
  }
  .variety-style {
    margin-top: 4px;
    font-size: 18px;
    color: var(--muted-grey);
    letter-spacing: 2px;
  }
  .edition {
    margin-top: 56px;
    line-height: 0.95;
    text-transform: uppercase;
  }
  .edition-brand {
    font-size: 82px;
    color: var(--logo-white);
    letter-spacing: -2px;
  }
  .edition-batch {
    font-size: 78px;
    color: var(--amber);
    letter-spacing: -2px;
  }
  .edition-number {
    font-size: 78px;
    color: var(--orange-deep);
  }
  .facts {
    margin-top: 60px;
    font-size: 18px;
    color: var(--logo-white);
    letter-spacing: 1px;
    line-height: 2;
  }
</style>
</head>
<body>
  <main class="label">
    <div class="brand">
      <span class="brand-dot"></span>
      <span class="brand-name">VELQUARTH</span>
    </div>

    <div class="variety">
      <p class="variety-flavour">ORANGE</p>
      <p class="variety-style">DRY GIN</p>
    </div>

    <h1 class="edition">
      <span class="edition-brand">Velquarth</span><br>
      <span class="edition-batch">Hollow Batch</span><br>
      <span class="edition-number">K7</span>
    </h1>

    <div class="facts">
      <p>43% VOL.</p>
      <p>0.5 LITERS</p>
    </div>
  </main>
</body>
</html>
```